Business card for utility of the future

I need a business card template designed for brivolo. We provide sustainable water, energy and waste services to homes.

The card should include name, position, email address, phone number, website and our logo (attached). I would like it to convey professionalism and creativity.

Target Market(s)

Homeowners, investors, corporate partners.

Industry/Entity Type

Utility

Contact Information for Business Card

The card should include name, position, email address, phone number, website and our logo (attached).

```html
<!DOCTYPE html>
<html lang="en">
<head>
<meta charset="UTF-8">
<title>brivolo – Business Card</title>
<link rel="stylesheet" href="https://fonts.googleapis.com/css2?family=Open+Sans:wght@400;600;700&display=swap">
<style>
  :root {
    --page-bg: #d8dbda;
    --card-bg: #eef1ef;
    --card-edge: #ffffff;
    --brand-green: #3f9d5c;
    --wave-green: #45a263;
    --accent-orange: #e2612c;
    --on-green: #ffffff;
    --tagline: #e4f1e8;
  }
  * { box-sizing: border-box; margin: 0; padding: 0; }
  html, body {
    width: 1200px; height: 970px; overflow: hidden;
    background: var(--page-bg);
    font-family: "Open Sans", Arial, sans-serif;
  }
  .canvas { position: relative; width: 1200px; height: 970px; }
  .card {
    position: absolute; left: 100px; top: 207px;
    width: 1000px; height: 556px;
    background: var(--card-bg);
    border: 1px solid var(--card-edge);
    border-radius: 26px;
    overflow: hidden;
    box-shadow: 0 10px 30px rgba(0,0,0,0.12);
  }
  .card__wave { position: absolute; inset: 0; width: 100%; height: 100%; }
  .brand-name {
    position: absolute; left: 48px; top: 96px;
    font-weight: 600; font-size: 62px; line-height: 1;
    color: var(--brand-green);
  }
  .person {
    position: absolute; right: 52px; top: 106px; text-align: right;
  }
  .person__name {
    font-weight: 700; font-size: 34px; letter-spacing: 1px;
    color: var(--brand-green); line-height: 1.15;
  }
  .person__role {
    font-size: 27px; color: var(--accent-orange); line-height: 1.2;
  }
  .address {
    position: absolute; right: 52px; top: 296px;
    text-align: right; color: var(--on-green);
    font-size: 24px; line-height: 1.22; font-style: normal;
  }
  .contact-list {
    position: absolute; right: 48px; top: 383px;
    list-style: none; color: var(--on-green);
    font-size: 24px; line-height: 34.5px;
  }
  .contact-list li {
    display: flex; justify-content: flex-end; align-items: center; gap: 10px;
  }
  .contact-list svg { width: 22px; height: 22px; fill: var(--on-green); flex: none; }
  .tagline {
    position: absolute; left: 48px; top: 460px;
    color: var(--tagline); font-size: 23.5px; line-height: 1.25;
  }
</style>
</head>
<body>
<main class="canvas">
  <section class="card" aria-label="brivolo business card">
    <svg class="card__wave" viewBox="0 0 1000 556" preserveAspectRatio="none" aria-hidden="true">
      <path d="M0,412 C230,440 380,385 520,300 C660,220 800,222 1000,232 L1000,556 L0,556 Z" fill="var(--wave-green)"/>
    </svg>

    <p class="brand-name">brivolo</p>

    <div class="person">
      <p class="person__name">LARS HOLMGREN</p>
      <p class="person__role">Founder</p>
    </div>

    <address class="address">
      2415 Alder Park Rd,<br>Harwick, MD 21340
    </address>

    <ul class="contact-list">
      <li>+ 000 000 0000
        <svg viewBox="0 0 24 24" aria-label="phone"><path d="M3 9c0-3 4-5 9-5s9 2 9 5l-4 1-1-3c-2-.6-6-.6-8 0l-1 3zM6 11h12l2 8H4z"/></svg>
      </li>
      <li>+ 000 000 0000
        <svg viewBox="0 0 24 24" aria-label="fax"><path d="M7 3h10v5H7zM3 9h18v8h-3v-3H6v3H3zM7 15h10v6H7z"/></svg>
      </li>
      <li>info@brivolo.com
        <svg viewBox="0 0 24 24" aria-label="email"><path d="M2 5h20v14H2z"/><path d="M3 6l9 7 9-7" fill="none" stroke="var(--wave-green)" stroke-width="2"/></svg>
      </li>
      <li>www.brivolo.com
        <svg viewBox="0 0 24 24" aria-label="website"><circle cx="12" cy="12" r="9" fill="none" stroke="var(--on-green)" stroke-width="2.4"/><path d="M12 3v18M3 12h18" stroke="var(--on-green)" stroke-width="2"/></svg>
      </li>
    </ul>

    <p class="tagline">provide sustainable water, energy and<br>waste services to homes.</p>
  </section>
</main>
</body>
</html>
```